Quilvo Garage Doors Business Card

I need a Business Card for my garage door business:
Quilvo Garage Doors.
please add:
logo
phone number: 855-3-QUILVO
(853-392)

email: service@quilvogaragedoors.com
website: www.quilvogaragedoors.com

The attached image is recommendation ONLY.

```html
<!DOCTYPE html>
<html lang="en">
<head>
<meta charset="utf-8">
<title>Quilvo Garage Doors – Business Card</title>
<link rel="stylesheet" href="https://fonts.googleapis.com/css2?family=Crimson+Text:wght@400;600&display=swap">
<style>
  :root {
    --page-bg: #e6e4e0;
    --card-white: #f1f0ee;
    --brand-blue: #4689b4;
    --brand-teal: #3aa9b5;
    --ink: #2c2c2c;
    --icon-dark: #333333;
    --photo-green-dark: #3c5a2e;
    --photo-green: #6f8a4a;
    --photo-road: #9a9c9a;
  }
  * { box-sizing: border-box; margin: 0; padding: 0; }
  html, body {
    width: 1200px; height: 1000px; overflow: hidden;
    background: var(--page-bg);
    font-family: "Crimson Text", Georgia, serif;
  }
  .sheet {
    position: relative; width: 1200px; height: 1000px;
  }
  .card {
    position: absolute; left: 250px; width: 700px; height: 400px;
    overflow: hidden;
    box-shadow: 0 6px 18px rgba(0,0,0,0.15);
  }
  .card--front { top: 70px; }
  .card--back { top: 530px; background: var(--card-white); }

  /* front side */
  .team-photo {
    position: absolute; inset: 0;
    background:
      linear-gradient(180deg, var(--photo-green-dark) 0%, var(--photo-green) 55%, #a7b09a 70%, var(--photo-road) 100%);
  }
  .front-band {
    position: absolute; top: 0; left: 0; width: 330px; height: 78px;
    background: var(--brand-blue);
    display: flex; align-items: center; gap: 14px; padding-left: 28px;
  }
  .brand-mark {
    width: 34px; height: 34px; background: var(--brand-teal); flex: none;
  }
  .brand-name {
    color: #ffffff; font-weight: 600; font-size: 22px; line-height: 1.05;
  }

  /* back side */
  .back-shape { position: absolute; inset: 0; }
  .back-logo {
    position: absolute; top: 36px; left: 56px;
    display: flex; align-items: center; gap: 16px;
  }
  .back-logo .brand-mark { width: 52px; height: 52px; }
  .back-logo .brand-name { color: var(--ink); font-size: 27px; }
  .contact-list {
    position: absolute; top: 180px; left: 60px;
    list-style: none; display: flex; flex-direction: column; gap: 16px;
  }
  .contact-item {
    display: flex; align-items: flex-start; gap: 14px;
    font-size: 22px; line-height: 1.1; color: var(--ink);
  }
  .contact-icon {
    width: 30px; height: 30px; border-radius: 50%;
    background: var(--icon-dark); flex: none;
    display: flex; align-items: center; justify-content: center;
  }
  .contact-item--web { font-weight: 600; }
</style>
</head>
<body>
<main class="sheet">
  <section class="card card--front">
    <div class="team-photo" role="img" aria-label="Photo of the service team standing beside a branded company pickup truck in front of trees"></div>
    <div class="front-band">
      <span class="brand-mark"></span>
      <span class="brand-name">Quilvo<br>Garage Doors</span>
    </div>
  </section>

  <section class="card card--back">
    <svg class="back-shape" width="700" height="400" viewBox="0 0 700 400" aria-hidden="true">
      <rect width="700" height="400" fill="var(--brand-blue)"/>
      <ellipse cx="170" cy="180" rx="355" ry="260" fill="var(--card-white)"/>
    </svg>
    <div class="back-logo">
      <span class="brand-mark"></span>
      <span class="brand-name">Quilvo<br>Garage Doors</span>
    </div>
    <ul class="contact-list">
      <li class="contact-item">
        <span class="contact-icon">
          <svg width="16" height="16" viewBox="0 0 24 24"><path fill="#fff" d="M6.6 10.8a15.1 15.1 0 0 0 6.6 6.6l2.2-2.2c.3-.3.7-.4 1-.2 1.1.4 2.3.6 3.6.6.6 0 1 .4 1 1V20c0 .6-.4 1-1 1A17 17 0 0 1 3 4c0-.6.4-1 1-1h3.5c.6 0 1 .4 1 1 0 1.3.2 2.5.6 3.6.1.3 0 .7-.2 1z"/></svg>
        </span>
        <span>855-3-QUILVO<br>(853-392)</span>
      </li>
      <li class="contact-item">
        <span class="contact-icon">
          <svg width="16" height="16" viewBox="0 0 24 24"><rect x="3" y="5" width="18" height="14" fill="none" stroke="#fff" stroke-width="2"/><path d="M3 6l9 7 9-7" fill="none" stroke="#fff" stroke-width="2"/></svg>
        </span>
        <span>service@quilvogaragedoors.com</span>
      </li>
      <li class="contact-item contact-item--web">
        <span class="contact-icon">
          <svg width="16" height="16" viewBox="0 0 24 24"><path fill="#fff" d="M12 3 2 12h3v8h5v-5h4v5h5v-8h3z"/></svg>
        </span>
        <span>www.quilvogaragedoors.com</span>
      </li>
    </ul>
  </section>
</main>
</body>
</html>
```